Dietetic office: Bright Plate

I want to give my business card a modern and warm look (which attracts the eye and has a reassuring side), which links dietetics to a moment of well-being. The front and back sides must be used (not just to put the logo on the front side)

The map should be eye-catching and easy to read. I don't necessarily want to have a plain background, which I find visually weighs down the maps.
I really like the square format of a business card with rounded edges which is different from what we are used to finding (and why not take this square diagonally?), however I am not closed to another format as long as I like the style.

Who am I? Mireille, 32 years old, Dietician and passionate about food since always. I am specialized in slimming and an expert in micro nutrition, which means that I take into account not only the nutritional balance while maintaining pleasure (if foods are present in the business card, I do not want some cliché things where there would just be fruits and vegetables, but really something more global), but also the psycho-emotional dimension that I will treat with food supplements based on plants, fruits or vegetables.

-----------------------------------------------------------------------------------

 Mention to appear on the card IN FRENCH (please be careful in case of translation that the use of words is correct):

Mireille DORAN
Dietician Nutritionist
Expert in Slimming and Micro-Nutrition

Slogan: I help you lose weight sustainably with pleasure and by reconciling your events

Catchphrases: Want to lose weight? Do you like going out? Do you have a lot of events? And is pleasure on your plate important to you?

Make an appointment on Rendiplan or on 06 41 58 30 92
mireille.brightplate@exemplo-mail.fr
Address: Health Center, Rue des Glycines, 13127 Vitrolles
www.brightplate-exemple.fr
Friendwall + Picturo Logo

- The company logo has been uploaded for your viewing. Other file formats can be made available if required.
- I would like a place for a photo of me to be possible.

Good morning,
I want to have a business card that is both lively and warm. Which will easily catch the eye while being easy to read and make people understand that I am in the field of well-being.
I like the square side in business cards (and why not use them diagonally?), or a more classic but original one.
Both the front and back sides must be used (I don't want to have the logo on just one side)
I don't want to have a plain background, but rather something more muted (I really like the suggestion from "Reed Cloud Graphic Designer" for this)
the use of logo for telephone, mail, address, rendiplan, friendwall, pictu etc is possible in order to facilitate reading

Please follow the various elements of the brief regarding the text and use the French text as it is.

I like business cards preferably square (with the possibility of using them diagonally).
The map should be eye-catching and easy to read.
It must bring pep while having softness which brings back to the well-being side
The card must be used on the front and back for the different elements (I do not want to have only the logo on the front side)
The text must correspond to the brief (be careful with the translation which can sometimes be bad)
I don't want to have a plain blue or orange background. I really like the idea of the background from "Reed Cloud Graphic Designer"

You can if you wish use symbols for contacts, telephone, rendiplan, address, fw, pictu....

Target Market(s)

mainly women between 25 and 65 years old + men around 40 years old

Contact Information for Business Card

Font styles to use
Sans Serif
Script

Colors
0054AA
0677BA
7BADD7
CADEEF
E8F1F8
0094D4
00A9DD
6FCCEA
C7EBF8
E9F6FB
00AB8E
00BBA5
67D7C9
C6EFE9
E9F9F6
FFC000
F8CF3A
FAE287
FDF2CF
FEFAEE
F0912C
F2A743
F7CA91
FBE8D2
FDF5EE

Requirements
Must have
• some pep! while being refined
Nice to have
• I really like the square format of a business card with rounded edges which is different from what we are used to finding, however I am not closed to another format as long as I like the style.
Should not have
• if foods are represented, only show fruits and vegetables (too cliché)

```html
<!DOCTYPE html>
<html lang="fr">
<head>
<meta charset="utf-8">
<title>Bright Plate – Business card</title>
<link href="https://fonts.googleapis.com/css2?family=Arimo:ital,wght@0,400;0,700;1,400&display=swap" rel="stylesheet">
<style>
  :root {
    --page-bg: #e4e4e4;
    --card-bg: #ffffff;
    --brand-blue: #0677BA;
    --deep-blue: #0677D4;
    --accent-orange: #F0912C;
    --bright-orange: #FF9900;
    --teal: #11CCE0;
    --ink: #222222;
    --white: #ffffff;
  }
  * { margin: 0; padding: 0; box-sizing: border-box; }
  html, body {
    width: 764px; height: 1200px; overflow: hidden;
    background: var(--page-bg);
    font-family: "Arimo", Arial, sans-serif;
  }
  .card {
    position: absolute;
    left: 157px;
    width: 461px; height: 461px;
    background: var(--card-bg);
    border-radius: 22px;
    overflow: hidden;
  }
  .card--front { top: 89px; }
  .card--back { top: 631px; }

  .social-links {
    position: absolute; top: 22px; right: 20px;
    display: flex; gap: 10px;
    font-size: 11px; font-weight: 700; color: var(--brand-blue);
  }
  .brand-name {
    position: absolute;
    font-weight: 400; color: var(--brand-blue);
    white-space: nowrap;
  }
  .card--front .brand-name { left: 32px; top: 82px; font-size: 34px; }
  .brand-dot {
    display: inline-block; width: 12px; height: 12px; border-radius: 50%;
    background: var(--accent-orange); margin-left: 8px; vertical-align: middle;
  }
  .person-name {
    position: absolute; left: 32px; top: 172px;
    font-size: 25px; font-weight: 700; color: var(--deep-blue);
  }
  .person-title {
    position: absolute; left: 33px; top: 206px;
    font-size: 15.5px; color: var(--accent-orange);
  }
  .person-expertise {
    position: absolute; left: 33px; top: 231px;
    font-size: 12.5px; color: var(--ink);
  }
  .slogan {
    position: absolute; left: 32px; top: 261px; width: 400px;
    font-size: 16.5px; font-style: italic; line-height: 22px;
    color: var(--bright-orange);
  }
  .contact-list { position: absolute; left: 32px; top: 327px; list-style: none; }
  .contact-item {
    display: flex; align-items: flex-start; gap: 10px;
    font-size: 15.5px; color: var(--ink); line-height: 20px;
  }
  .contact-item + .contact-item { margin-top: 6px; }
  .contact-item--address { margin-bottom: 4px; }
  .contact-icon { width: 16px; height: 18px; flex: none; margin-top: 1px; }

  .back-art { position: absolute; inset: 0; width: 461px; height: 461px; }
  .catchphrases {
    position: absolute; left: 29px; top: 40px; width: 262px;
    list-style: none; color: var(--white);
    font-size: 24px; font-style: italic; line-height: 25px;
  }
  .catchphrases li + li { margin-top: 6px; }
  .card--back .brand-name { left: 134px; top: 326px; font-size: 44px; }
  .appointment-band {
    position: absolute; left: 0; bottom: 0; width: 100%; height: 41px;
    background: var(--teal); color: var(--white);
    font-size: 14px; font-weight: 700;
    padding-left: 29px; line-height: 40px;
  }
</style>
</head>
<body>

<section class="card card--front">
  <div class="social-links"><span>Picturo</span><span>Friendwall</span></div>
  <div class="brand-name">Bright Plate<span class="brand-dot"></span></div>

  <h1 class="person-name">Mireille DORAN</h1>
  <p class="person-title">Dietician Nutritionist</p>
  <p class="person-expertise">Expert in Slimming and Micro-Nutrition</p>

  <p class="slogan">I help you lose weight sustainably with pleasure and by reconciling your events</p>

  <ul class="contact-list">
    <li class="contact-item contact-item--address">
      <svg class="contact-icon" viewBox="0 0 16 18" aria-hidden="true">
        <path d="M8 0a6 6 0 0 0-6 6c0 4.5 6 12 6 12s6-7.5 6-12a6 6 0 0 0-6-6z" fill="var(--teal)"/>
        <circle cx="8" cy="6" r="2.4" fill="#fff"/>
      </svg>
      <span>Health Center<br>Rue des Glycines, 13127 Vitrolles</span>
    </li>
    <li class="contact-item">
      <svg class="contact-icon" viewBox="0 0 16 18" aria-hidden="true">
        <rect x="1" y="5" width="14" height="10" fill="var(--teal)"/>
        <path d="M1.5 5.5 8 11l6.5-5.5" fill="none" stroke="#fff" stroke-width="1.2"/>
      </svg>
      <span>mireille.brightplate@exemplo-mail.fr</span>
    </li>
    <li class="contact-item">
      <svg class="contact-icon" viewBox="0 0 16 18" aria-hidden="true">
        <circle cx="8" cy="10" r="7" fill="var(--teal)"/>
        <path d="M4 7c2 0 2 2 3 3s-1 3 0 4M10 4c0 2 2 2 3 3" fill="none" stroke="#fff" stroke-width="1.3"/>
      </svg>
      <span>www.brightplate-exemple.fr</span>
    </li>
  </ul>
</section>

<section class="card card--back">
  <svg class="back-art" viewBox="0 0 461 461" aria-hidden="true">
    <path d="M0 0H387C372 150 252 282 0 334Z" fill="var(--deep-blue)"/>
    <path d="M392 0H433C420 170 282 304 0 341V337C256 284 378 152 392 0Z" fill="var(--bright-orange)"/>
  </svg>
  <ul class="catchphrases">
    <li>Want to lose weight?</li>
    <li>Do you like going out?</li>
    <li>Do you have a lot of events?</li>
    <li>And the pleasure on your plate is important to you?</li>
  </ul>
  <div class="brand-name">Bright Plate<span class="brand-dot"></span></div>
  <p class="appointment-band">Make an appointment on Rendiplan or on 06 41 58 30 92</p>
</section>

</body>
</html>
```